Glen Holbrook Announces his new career move! 8x5 card please.

Associate Broker GLEN HOLBROOK is proud to announce his new affiliation with m.vorlund bayshore estates, ltd.

His goal remains to meet all your real estate needs. Prepare to renew your seasonal rental for 2016...with the full support of his new office, Glen can handle your renewal seamlessly.

Prepared to purchase? With access to every property on the market...Glen can show you how easy it making your summer dreams come true can be.

Thinking about selling? m.vorlund bayshore estates, ltd. now offers the benefits of the Multiple Listing Service (MLS) to all sellers. In cooperation with MLS Sellers receive the maximum worldwide exposure, Purchasers receive a larger volume of properties to view and in cooperation with other Realtors, the transaction is handled professionally!!!!

I will send logo and photo of Glen Holbrook separately. Thank you. P-
Updates

Target Market(s)

Tenants, Sellers & Buyers

Industry/Entity Type

Broker

Font styles to use
Sans Serif

Requirements
Must have
• I attached logo and photo of Glen. Added a better photo of Glen.
Nice to have
• A photo of a property we have listed. I added a couple to choose from.
Should not have
• No Red color

```html
<!DOCTYPE html>
<html lang="en">
<head>
<meta charset="utf-8">
<title>Glen Holbrook – Announcement Card</title>
<link href="https://fonts.googleapis.com/css2?family=Lato:ital,wght@0,400;0,700;0,900;1,400&display=swap" rel="stylesheet">
<style>
  :root{
    --page:#ffffff;
    --ink:#1d1d1d;
    --orange:#ee8f22;
    --panel:#242424;
    --sand-light:#e2d3ba;
    --sand-dark:#c9b491;
    --mauve:#8e6f82;
    --teal:#2f9aa6;
    --teal-dark:#187a77;
    --stone:#b6b2a6;
    --sky:#7cb7d3;
    --sky-pale:#aad5ea;
    --sage:#7fae89;
    --jade:#5aa27e;
    --grey:#c4c4c4;
    --slate:#6d8898;
  }
  *{box-sizing:border-box;margin:0;padding:0}
  html,body{width:927px;height:1200px;overflow:hidden;background:var(--page)}
  body{position:relative;font-family:"Lato",Arial,sans-serif;color:var(--ink)}

  .card{position:absolute;left:99px;width:722px;height:519px;box-shadow:3px 4px 7px rgba(0,0,0,.28);overflow:hidden}
  .card--front{top:60px;background:linear-gradient(160deg,var(--sand-light),var(--sand-dark) 55%,var(--sand-light))}
  .card--back{top:620px;background:#fff}

  .tile-grid{position:absolute;left:0;top:0;width:722px;height:310px;display:grid;grid-template-columns:repeat(7,1fr);grid-template-rows:repeat(3,1fr)}
  .tile{width:100%;height:100%}
  .tile--mauve{background:var(--mauve)}
  .tile--teal{background:var(--teal)}
  .tile--teal-dark{background:var(--teal-dark)}
  .tile--stone{background:var(--stone)}
  .tile--sky{background:var(--sky)}
  .tile--sky-pale{background:var(--sky-pale)}
  .tile--sage{background:var(--sage)}
  .tile--jade{background:var(--jade)}
  .tile--grey{background:var(--grey)}
  .tile--slate{background:var(--slate)}
  .photo{}
  .photo--boardwalk{background:linear-gradient(180deg,#a9b9c4,#8c9a6e 60%,#b8a98a)}
  .photo--night-house{background:linear-gradient(180deg,#4b4450,#c98a4c 55%,#6e4a3a)}
  .photo--deck{background:linear-gradient(180deg,#c6d3de,#6e7a80 55%,#3f4448)}
  .photo--ceiling{background:linear-gradient(135deg,#b68a63,#8a5e3c 60%,#d1b190)}
  .photo--garden-house{background:linear-gradient(180deg,#dbe5ec,#7a8d6a 55%,#4f6b3f)}
  .photo--pool{background:linear-gradient(180deg,#4fa3c9,#29a8d8 50%,#7fd0ea)}
  .photo--modern-house{background:linear-gradient(180deg,#9fb3c2,#e3e1da 55%,#8d8a80)}
  .photo--umbrellas{background:linear-gradient(160deg,#e8e8e2,#6b6b66 55%,#3e3e3a)}
  .photo--living{background:linear-gradient(180deg,#d9e3e6,#a9b7b5 50%,#eae7df)}
  .photo--ocean-room{background:linear-gradient(180deg,#b7cddd,#5e8db1 45%,#c9b48e 70%,#8b6f4c)}

  .feature{position:absolute;left:254px;top:156px;width:223px;height:353px}
  .feature svg{position:absolute;left:0;top:0}
  .feature__banner{position:absolute;left:-11px;top:25px;width:251px;height:46px;background:var(--orange);color:#fff;text-align:center}
  .feature__role{display:block;font-size:11.5px;letter-spacing:.5px;padding-top:5px;line-height:13px}
  .feature__name{display:block;font-size:21px;font-weight:900;letter-spacing:.8px;line-height:24px}
  .feature__note{position:absolute;left:0;top:82px;width:223px;text-align:center;color:#fff;font-style:italic;font-size:11.5px;line-height:14px}
  .feature__portrait{position:absolute;left:43px;top:122px;width:126px;height:128px;background:radial-gradient(ellipse at 50% 35%,#8a6a58 0 30%,#3a3230 60%,#242424 80%)}

  .note{position:absolute;top:350px;height:133px;background:rgba(255,255,255,.55)}
  .note--about{left:44px;width:195px;padding:16px 0 0 14px;font-size:13.3px;font-weight:700;line-height:16.4px}
  .note--contact{left:517px;width:179px;padding:26px 0 0 12px;font-size:13px;font-weight:700}
  .note--contact p{margin-bottom:18px}
  .note--contact .label{font-weight:400;margin-right:4px}

  .brand{position:absolute;left:30px;top:25px;display:flex;align-items:center;gap:7px;font-size:15px;font-weight:700;color:var(--ink);letter-spacing:-.2px}
  .brand__mark{width:9px;height:9px;background:var(--teal-dark)}
  .copy{position:absolute;left:33px;width:240px;font-size:14.3px;line-height:18.8px}
  .copy h2{color:var(--orange);font-size:14.3px;font-weight:700;line-height:18.8px}
  .copy--buy{top:111px}
  .copy--sell{top:213px}
  .rule{position:absolute;left:33px;top:417px;width:117px;height:4px;background:var(--orange)}
  .contact{position:absolute;left:33px;top:431px;font-size:12.5px;font-weight:700;line-height:20px}
  .contact .label{color:#8a8a8a;font-weight:700;margin-right:3px}
</style>
</head>
<body>

<section class="card card--front" aria-label="Announcement card front">
  <div class="tile-grid">
    <div class="tile photo photo--boardwalk" role="img" aria-label="Photo of a boardwalk to a beach house"></div>
    <div class="tile photo photo--night-house" role="img" aria-label="Photo of a lit house at dusk"></div>
    <div class="tile tile--mauve"></div>
    <div class="tile photo photo--deck" role="img" aria-label="Photo of an ocean-view deck"></div>
    <div class="tile photo photo--ceiling" role="img" aria-label="Photo of a wood ceiling with fan"></div>
    <div class="tile tile--teal"></div>
    <div class="tile photo photo--garden-house" role="img" aria-label="Photo of a house with garden"></div>

    <div class="tile tile--stone"></div>
    <div class="tile tile--teal-dark"></div>
    <div class="tile photo photo--pool" role="img" aria-label="Photo of a swimming pool"></div>
    <div class="tile tile--slate"></div>
    <div class="tile photo photo--modern-house" role="img" aria-label="Photo of a modern beach house"></div>
    <div class="tile photo photo--umbrellas" role="img" aria-label="Photo of patio umbrellas"></div>
    <div class="tile tile--sky"></div>

    <div class="tile tile--sage"></div>
    <div class="tile photo photo--living" role="img" aria-label="Photo of a bright living room"></div>
    <div class="tile tile--grey"></div>
    <div class="tile tile--grey"></div>
    <div class="tile tile--jade"></div>
    <div class="tile tile--sky-pale"></div>
    <div class="tile photo photo--ocean-room" role="img" aria-label="Photo of a room overlooking the ocean"></div>
  </div>

  <div class="note note--about">His goal remains to meet all your real estate needs. Prepare to renew your seasonal rental for 2016... with the full support of his new office, Glen can handle your renewal seamlessly.</div>

  <div class="note note--contact">
    <p>bayshoreestates.com</p>
    <p><span class="label">Ph</span>555.204.7300</p>
    <p><span class="label">C</span> 555.318.6642</p>
  </div>

  <div class="feature">
    <svg width="223" height="353" viewBox="0 0 223 353" aria-hidden="true">
      <path d="M14 0 H209 A14 14 0 0 0 223 14 V339 A14 14 0 0 0 209 353 H14 A14 14 0 0 0 0 339 V14 A14 14 0 0 0 14 0 Z" fill="#242424"/>
      <path d="M20 7 H203 A13 13 0 0 0 216 20 V333 A13 13 0 0 0 203 346 H20 A13 13 0 0 0 7 333 V20 A13 13 0 0 0 20 7 Z" fill="none" stroke="#fff" stroke-width="1.6"/>
    </svg>
    <div class="feature__banner">
      <span class="feature__role">ASSOCIATE BROKER</span>
      <span class="feature__name">GLEN HOLBROOK</span>
    </div>
    <p class="feature__note">is proud to announce his new<br>affiliation with<br>m.vorlund bayshore estates, ltd.</p>
    <div class="feature__portrait" role="img" aria-label="Portrait photo of Glen Holbrook"></div>
  </div>
</section>

<section class="card card--back" aria-label="Announcement card back">
  <div class="brand"><span>m.vorlund bayshore estates, ltd.</span><span class="brand__mark"></span></div>

  <div class="copy copy--buy">
    <h2>Prepared to purchase?</h2>
    <p>With access to every property on the market...Glen can show you how easy it making your summer dreams come true can be.</p>
  </div>

  <div class="copy copy--sell">
    <h2>Thinking about selling?</h2>
    <p>m.vorlund bayshore estates, ltd. now offers the benefits of the Multiple Listing Service (MLS) to all sellers. In cooperation with MLS Sellers receive the maximum worldwide exposure, Purchasers receive a larger volume of properties to view and in cooperation with other Realtors, the transaction is handled professionally!!!!</p>
  </div>

  <div class="rule"></div>
  <div class="contact">
    <p>bayshoreestates.com</p>
    <p><span class="label">Ph</span>555.204.7300</p>
    <p><span class="label">C</span> 555.318.6642</p>
  </div>
</section>

</body>
</html>
```